New modern and animated Design needed for a portal login site (Relaymark Portal)

Relaymark is software for market communication B2B & EAI.
We need a modern look for a Relaymark Portal login site. We prefer a full size use for the background design of the login-page, with animation.
The name of the site is “Relaymark Langzeitarchiv”, what should appear as text. Further there is space needed for the login name and password.
Responsive Design is required.
We have a new Relaymark logo (find attached), that can be used for the animation, for example but not necessarily.
Feel free to visit our website for inspiration (colours etc.): www.vornelsystems.de.

Reason: Can you please animate the backgraound and send links to view it.

Reason: there is aproblem with pitchforge - we acually cannot view any designs

Target Market(s)

energy sector, IT

Industry/Entity Type

Communication

Number of Pages Required

1 page

Font styles to use
Sans Serif

Colors

Designer to choose colors to be used in the design.

Requirements
Must have
• fullscreen background design (like "onepager"),
• animated (infinity), not to much action
• the only text that is needed is "Relaymark Langzeitarchiv" (in front) and the login details: "Benutzername" (+ space for the username (free position)) and "Paswort" (+ space for the password (free position))
Nice to have
• maybe shades of blue, or colours, like the ones used on our website and logo (vornel systems) or Relaymark icon (files named "asset")
• animation can also be a film that starts over and over again (note: The up half of the page www.mirtobanu.de is one example, which is nice to watch - but here it is not necessary to use a movie)

```html
<!DOCTYPE html>
<html lang="de">
<head>
<meta charset="utf-8">
<title>Relaymark Langzeitarchiv – Login</title>
<link rel="stylesheet" href="https://fonts.googleapis.com/css2?family=Oswald:wght@400&family=Open+Sans:wght@400;700&display=swap">
<style>
  :root {
    --brand-blue: #1259a6;
    --brand-dark: #145d94;
    --frame-blue: #1a5aa3;
    --field-bg: #f7f7f7;
    --field-border: #b8bcc2;
    --text-dark: #333;
    --text-muted: #555;
    --bg-top: #d7dce2;
    --bg-mid: #e4e7eb;
    --bg-bottom: #f2f3f5;
  }
  * { box-sizing: border-box; margin: 0; padding: 0; }
  html, body { width: 1200px; height: 679px; overflow: hidden; }
  body { font-family: "Open Sans", sans-serif; color: var(--text-dark); }

  .login-page { position: relative; width: 1200px; height: 679px; overflow: hidden; }

  .backdrop {
    position: absolute; inset: 0;
    background:
      radial-gradient(ellipse 60% 50% at 55% 35%, rgba(255,255,255,0.55), transparent 70%),
      linear-gradient(180deg, var(--bg-top) 0%, var(--bg-mid) 55%, var(--bg-bottom) 100%);
  }

  .brand {
    position: absolute; left: 390px; top: 70px; width: 422px; height: 95px;
    display: flex; align-items: center; gap: 18px;
  }
  .brand-mark { width: 88px; height: 88px; border-radius: 50%; background: var(--brand-dark); flex: none; }
  .brand-name {
    font-family: "Open Sans", sans-serif; font-weight: 400; font-size: 44px;
    line-height: 42px; color: var(--brand-dark);
  }

  .login-frame {
    position: absolute; left: 330px; top: 244px; width: 541px; height: 258px;
    border: 2px solid var(--frame-blue); border-top: none;
  }
  .login-frame::before, .login-frame::after {
    content: ""; position: absolute; top: 0; height: 2px; width: 38px; background: var(--frame-blue);
  }
  .login-frame::before { left: -2px; }
  .login-frame::after { right: -2px; }

  .site-title {
    position: absolute; left: 0; right: 0; top: -24px; text-align: center;
    font-family: "Oswald", sans-serif; font-weight: 400; font-size: 38px; line-height: 46px;
    color: var(--brand-blue); letter-spacing: 0.2px;
  }

  .field {
    position: absolute; left: 104px; width: 328px; height: 40px;
    border: 1px solid var(--field-border); border-radius: 20px; background: var(--field-bg);
    display: flex; align-items: center;
  }
  .field-user { top: 52px; }
  .field-pass { top: 104px; }
  .field-icon {
    width: 42px; height: 100%; display: flex; align-items: center; justify-content: center;
    border-right: 1px solid #dcdcdc;
  }
  .field-label { padding-left: 12px; font-size: 13px; color: var(--text-muted); }

  .login-button {
    position: absolute; left: 104px; top: 155px; width: 328px; height: 40px;
    border: 1px solid #3d86cf; border-radius: 20px; background: var(--brand-blue);
    color: #fff; font-family: "Open Sans", sans-serif; font-weight: 700; font-size: 18px;
    display: flex; align-items: center; justify-content: center; letter-spacing: 0.5px;
  }

  .signup-note {
    position: absolute; left: 0; right: 0; top: 219px; text-align: center;
    font-size: 11px; color: #222;
  }

  .social-row {
    position: absolute; left: 526px; top: 553px; display: flex; gap: 4px;
  }
  .social-dot { width: 26px; height: 26px; border: 1.5px solid #4a86c5; border-radius: 50%; }

  .copyright {
    position: absolute; left: 0; right: 0; top: 592px; text-align: center;
    font-size: 12.5px; color: #333;
  }
  .build-tag { position: absolute; left: 1154px; top: 607px; font-size: 12px; color: #333; }
</style>
</head>
<body>
<main class="login-page">
  <div class="backdrop" role="img" aria-label="Soft light office photograph: city skyline through windows, laptop and coffee cup on a white desk"></div>

  <header class="brand">
    <span class="brand-mark"></span>
    <span class="brand-name">vornel<br>systems</span>
  </header>

  <section class="login-frame">
    <h1 class="site-title">RELAYMARK LANGZEITARCHIV</h1>

    <div class="field field-user">
      <span class="field-icon">
        <svg width="13" height="14" viewBox="0 0 13 14"><circle cx="6.5" cy="4" r="3.3" fill="#555"/><path d="M0.5 14 C0.5 9 3 7.8 6.5 7.8 S12.5 9 12.5 14 Z" fill="#555"/></svg>
      </span>
      <span class="field-label">Benutzername</span>
    </div>

    <div class="field field-pass">
      <span class="field-icon">
        <svg width="13" height="15" viewBox="0 0 13 15"><path d="M3 7 V4.5 A3.5 3.5 0 0 1 10 4.5" fill="none" stroke="#555" stroke-width="1.8"/><rect x="1" y="7" width="11" height="8" rx="1" fill="#555"/></svg>
      </span>
      <span class="field-label">Paswort</span>
    </div>

    <div class="login-button">LOGIN</div>
    <p class="signup-note">Not a member? Sign up now!</p>
  </section>

  <nav class="social-row" aria-label="Social links">
    <span class="social-dot"></span><span class="social-dot"></span><span class="social-dot"></span><span class="social-dot"></span><span class="social-dot"></span>
  </nav>

  <footer class="copyright">© 2017 vornel systems . All rights reserved.</footer>
  <span class="build-tag">C7</span>
</main>
</body>
</html>
```